Estate Planner needs an Ad for a local newsletter

I need an ad designed for my practice as an estate planning attorney. The ad will be in a newsletter that targets individuals over the age of 55. My ad is 7.5"W x 4.6"H (a half page ad) .
The wording should include:
Varnholt, Danielle

Danielle Varnholt

Wisdom Meets Planning
Your Estate, Your Legacy

After 23 years as a military spouse, moving our family of six across the country,
I learned the true value of careful planning. Today I help Palomar County's seniors protect what matters most – their family’s future and their life’s work.

I understand that your estate is more than just assets – it's a lifetime of wise
decisions, cherished memories, and dreams for your family's future.

Professional Estate Planning:
• Wills & Living Trusts • Healthcare Directives
• Power of Attorney • Asset Protection
• Probate Avoidance • Peace of Mind

Plus also needs to have my contact information:
RPV Law
Danielle Varnholt
Attorney/Of Counsel
4712 Cedarbrook Lane
Lakemont, Florida 32990
(555) 684-1093
dvarnholt@rpvlegalteam.example
Logo is attached.

```html
<!DOCTYPE html>
<html lang="en">
<head>
<meta charset="utf-8">
<title>RPV Law – Estate Planning Ad</title>
<link rel="stylesheet" href="https://fonts.googleapis.com/css2?family=Open+Sans:wght@300;400;600;800&display=swap">
<style>
  :root {
    --page-bg: #dcdddf;
    --navy: #1c2640;
    --blue: #12457f;
    --white: #ffffff;
    --soft-text: #dbe4f1;
    --photo-light: #efe9e0;
    --photo-mid: #c9b9a4;
    --portrait-light: #e4e2df;
    --portrait-mid: #8b7a6c;
  }
  * { box-sizing: border-box; margin: 0; padding: 0; }
  html, body {
    width: 927px; height: 1200px; overflow: hidden;
    background: var(--page-bg);
    font-family: "Open Sans", sans-serif;
  }
  .ad {
    position: absolute; left: 34px; top: 336px;
    width: 860px; height: 527px; overflow: hidden;
    background: var(--navy);
  }
  .hero-photo {
    position: absolute; left: 0; top: 0; width: 660px; height: 420px;
    background: linear-gradient(120deg, var(--photo-light) 0%, #f6f2ec 40%, var(--photo-mid) 100%);
  }
  .contact-panel {
    position: absolute; left: 654px; top: 0; width: 206px; height: 527px;
    background: var(--navy);
    clip-path: polygon(8px 0, 100% 0, 100% 100%, 0 100%, 0 10px);
    color: var(--white); text-align: center;
  }
  .brand { margin-top: 28px; }
  .brand-name {
    font-weight: 600; font-size: 28px; letter-spacing: 0.5px; line-height: 1;
  }
  .brand-partners { font-size: 6.5px; font-weight: 600; margin-top: 6px; }
  .brand-est { font-size: 6px; font-weight: 600; margin-top: 3px; letter-spacing: 0.4px; }
  .tagline {
    margin-top: 14px; font-weight: 800; font-size: 12.5px; line-height: 1.4;
  }
  .attorney-name { margin-top: 9px; font-weight: 800; font-size: 12.5px; }
  .contact-line { font-weight: 300; font-size: 12.5px; line-height: 1.4; }
  .contact-line.role { margin-bottom: 7px; }
  .contact-line.gap { margin-top: 7px; }
  .contact-line.email { font-size: 11.5px; }
  .blue-band {
    position: absolute; left: 0; top: 384px; width: 662px; height: 143px;
    background: var(--blue);
  }
  .services {
    position: absolute; left: 0; top: 309px; width: 396px; height: 108px;
    background: var(--navy);
    clip-path: polygon(0 0, 380px 0, 100% 22px, 100% 92px, 384px 100%, 0 100%);
    color: var(--white);
    padding: 12px 0 0 42px;
  }
  .services-title { font-weight: 800; font-size: 19px; line-height: 1.2; }
  .services-list {
    list-style: none; display: grid; grid-template-columns: 179px auto;
    font-weight: 300; font-size: 16.5px; line-height: 19px; margin-top: 3px;
    white-space: nowrap;
  }
  .services-list li::before { content: "•"; font-size: 10px; vertical-align: 2px; margin-right: 5px; }
  .story {
    position: absolute; left: 44px; top: 423px; width: 600px;
    color: var(--soft-text); font-weight: 300; font-size: 14.4px; line-height: 17.3px;
    white-space: nowrap;
  }
  .story p + p { margin-top: 6px; }
  .portrait {
    position: absolute; left: 597px; top: 276px; width: 256px; height: 219px;
    background: linear-gradient(160deg, var(--portrait-light) 0%, #cfc8c0 55%, var(--portrait-mid) 100%);
    clip-path: polygon(25% 0, 75% 0, 100% 50%, 75% 100%, 25% 100%, 0 50%);
  }
</style>
</head>
<body>
  <section class="ad">
    <div class="hero-photo" role="img" aria-label="Photo of a smiling senior couple reviewing a home budget on a laptop with an advisor holding a clipboard"></div>

    <div class="blue-band"></div>

    <div class="services">
      <h2 class="services-title">Professional Estate Planning:</h2>
      <ul class="services-list">
        <li>Wills &amp; Living Trusts</li><li>Asset Protection</li>
        <li>Healthcare Directives</li><li>Probate Avoidance</li>
        <li>Power of Attorney</li><li>Peace of Mind</li>
      </ul>
    </div>

    <div class="story">
      <p>After 23 years as a military spouse, moving our family of six across the country,<br>I learned the true value of careful planning. Today I help Palomar County’s seniors<br>protect what matters most – their family’s future and their life’s work.</p>
      <p>I understand that your estate is more than just assets – it’s a lifetime of wise decisions,<br>cherished memories, and dreams for your family’s future.</p>
    </div>

    <aside class="contact-panel">
      <div class="brand">
        <div class="brand-name">RPV Law</div>
        <div class="brand-partners">Rowland · Pierce · Voss · Hale · Marsh</div>
        <div class="brand-est">EST. 1976</div>
      </div>
      <p class="tagline">Wisdom Meets Planning<br>Your Estate, Your Legacy</p>
      <p class="attorney-name">Danielle Varnholt</p>
      <p class="contact-line role">Attorney / Of Counsel</p>
      <p class="contact-line">4712 Cedarbrook Lane</p>
      <p class="contact-line">Lakemont, Florida 32990</p>
      <p class="contact-line gap">(555) 684-1093</p>
      <p class="contact-line email">dvarnholt@rpvlegalteam.example</p>
    </aside>

    <div class="portrait" role="img" aria-label="Portrait photo of attorney Danielle Varnholt"></div>
  </section>
</body>
</html>
```